Business Card Design

Hoping for a black background business card, minimalistic design.
With the Marble Crest logo you created in white.

I would like to include:
My Name and title
Address (street address)
Reception: (phone number)
Fax: (fax number)
Reception: (email address)
Direct email: (email address)
Instagram: (ig handle)

```html
<!DOCTYPE html>
<html lang="en">
<head>
<meta charset="utf-8">
<title>Marble Crest — Business Card</title>
<link rel="stylesheet" href="https://fonts.googleapis.com/css2?family=Poppins:wght@300;400;500;600&display=swap">
<style>
  :root {
    --backdrop: #1c1c1c;
    --card-dark: #000000;
    --card-light: #ffffff;
    --ink-light: #ffffff;
    --ink-dark: #111111;
    --rule-light: rgba(255,255,255,0.85);
  }
  * { margin: 0; padding: 0; box-sizing: border-box; }
  html, body { width: 1200px; height: 1015px; overflow: hidden; }
  body {
    background: var(--backdrop);
    font-family: "Poppins", sans-serif;
    display: flex;
    flex-direction: column;
    align-items: center;
    justify-content: center;
    gap: 56px;
  }
  .card {
    position: relative;
    width: 630px;
    height: 360px;
    box-shadow: 0 14px 40px rgba(0,0,0,0.55);
  }

  /* Front */
  .card--front { background: var(--card-dark); color: var(--ink-light); }
  .brand {
    position: absolute;
    left: 118px; top: 118px;
    display: flex; align-items: center; gap: 22px;
  }
  .brand__circle {
    width: 92px; height: 92px;
    border: 4px solid var(--ink-light);
    border-radius: 50%;
  }
  .brand__divider {
    width: 1.5px; height: 100px;
    background: var(--rule-light);
  }
  .brand__name {
    font-size: 38px; font-weight: 400;
    letter-spacing: 0.12em; text-transform: uppercase;
    line-height: 1;
  }
  .rule {
    position: absolute; height: 1px; background: var(--rule-light);
  }
  .rule--top { left: 380px; top: 100px; width: 170px; }
  .rule--left { left: 140px; top: 286px; width: 140px; }
  .rule--right { left: 430px; top: 286px; width: 140px; }
  .social {
    position: absolute; left: 300px; top: 272px;
    display: flex; align-items: center; gap: 10px;
    font-size: 18px; font-weight: 300;
  }
  .social__dot {
    width: 20px; height: 20px; border-radius: 50%;
    background: #c13584;
  }

  /* Back */
  .card--back { background: var(--card-light); color: var(--ink-dark); }
  .person { position: absolute; left: 44px; top: 56px; }
  .person__name { font-size: 24px; font-weight: 600; letter-spacing: 0.03em; line-height: 1.1; }
  .person__title { font-size: 17px; font-weight: 400; }
  .address {
    position: absolute; left: 44px; top: 150px;
    font-size: 17px; line-height: 1.3;
  }
  .contacts {
    position: absolute; left: 44px; top: 232px;
    list-style: none; font-size: 17px; line-height: 1.45;
  }
  .contacts li { display: flex; align-items: center; gap: 8px; }
  .contacts svg { width: 20px; height: 20px; flex: none; }
  .seal {
    position: absolute; right: 46px; top: 44px;
    width: 250px; height: 250px;
    border: 12px solid var(--ink-dark);
    border-radius: 50%;
    display: flex; align-items: center; justify-content: center;
    text-align: center;
    font-size: 30px; font-weight: 500; letter-spacing: 0.08em;
    text-transform: uppercase; line-height: 1.15;
  }
</style>
</head>
<body>

<section class="card card--front" aria-label="Card front">
  <div class="rule rule--top"></div>
  <div class="brand">
    <div class="brand__circle"></div>
    <div class="brand__divider"></div>
    <div class="brand__name">Marble Crest</div>
  </div>
  <div class="rule rule--left"></div>
  <div class="social"><span class="social__dot"></span><span>ig handle</span></div>
  <div class="rule rule--right"></div>
</section>

<section class="card card--back" aria-label="Card back">
  <div class="person">
    <div class="person__name">DANIEL HARPER</div>
    <div class="person__title">Managing Director</div>
  </div>
  <div class="address">421, Address line goes here<br>45452,Country Name</div>
  <ul class="contacts">
    <li>
      <svg viewBox="0 0 20 20" aria-hidden="true"><circle cx="10" cy="10" r="9" fill="none" stroke="#111" stroke-width="1.4"/><path d="M7 6l2 2-1 1.2a5 5 0 0 0 2.8 2.8L12 11l2 2-1.2 1.2C9.5 14 6 10.5 5.8 7.2z" fill="#111"/></svg>
      044-321 654 870
    </li>
    <li>
      <svg viewBox="0 0 20 20" aria-hidden="true"><circle cx="10" cy="10" r="9" fill="none" stroke="#111" stroke-width="1.4"/><rect x="7" y="5" width="6" height="3.5" fill="#111"/><rect x="5" y="8.5" width="10" height="5" rx="1" fill="#111"/><rect x="7" y="12" width="6" height="3.5" fill="#fff" stroke="#111" stroke-width="1"/></svg>
      044-321 654 871
    </li>
    <li>
      <svg viewBox="0 0 20 20" aria-hidden="true"><circle cx="10" cy="10" r="9" fill="none" stroke="#111" stroke-width="1.4"/><rect x="5" y="6.5" width="10" height="7" fill="#111"/><path d="M5 6.5l5 4 5-4" fill="none" stroke="#fff" stroke-width="1"/></svg>
      info@marblecrest.com (Reception)
    </li>
    <li>
      <svg viewBox="0 0 20 20" aria-hidden="true"><circle cx="10" cy="10" r="9" fill="none" stroke="#111" stroke-width="1.4"/><rect x="5" y="6.5" width="10" height="7" fill="#111"/><path d="M5 6.5l5 4 5-4" fill="none" stroke="#fff" stroke-width="1"/></svg>
      info@marblecrest.com(Direct)
    </li>
  </ul>
  <div class="seal">Marble<br>Crest</div>
</section>

</body>
</html>
```